I need 4 Power Point foils for 4 companies.
1 Folis for TeskaPoint, 1 Foils for Luxury, 1 Folis for Hospitality Group and the mother of Teska and Luxury is Hospitality. So we also need a foil as head hospitality and you have to realize that the other companies belong to it. I would like a cover sheet and a presentation templates.
Updates
Hey i Need for My companies Presentation Cover and Template thank you
Target Market(s)
Travel industry
Colors
Designer to choose only greyscale colors for use in the design.
Requirements
Must have
- create your own design

```html
<!DOCTYPE html>
<html lang="en">
<head>
<meta charset="utf-8">
<title>Meridian Hospitality Group – Presentation Template</title>
<link href="https://fonts.googleapis.com/css2?family=Bebas+Neue&family=Open+Sans:wght@300;400;600;700&family=Montserrat:wght@400;500&display=swap" rel="stylesheet">
<style>
:root{
  --page:#ffffff;
  --ink:#56606a;
  --panel:#6b6d6f;
  --panel-light:#7e7f80;
  --night:#23221c;
  --paper:#f1f1f1;
  --gold:#c4a35a;
  --heading:#4b4b47;
  --olive:#5a5636;
  --muted:#8a8a86;
  --white:#ffffff;
}
*{box-sizing:border-box;margin:0;padding:0}
html,body{width:1200px;height:2194px;overflow:hidden;background:var(--page)}
body{position:relative;font-family:"Open Sans",Arial,sans-serif;color:var(--heading)}

.brand-mark{position:absolute;left:89px;top:128px;display:flex;align-items:center;gap:16px}
.brand-mark .dot{width:58px;height:58px;border:3px solid var(--ink);border-radius:50%;flex:none}
.brand-mark .name{font-family:"Open Sans",Arial,sans-serif;font-weight:600;font-size:24px;line-height:1.15;color:var(--ink);width:180px}
.sheet-title{position:absolute;left:399px;top:112px;font-family:"Bebas Neue",Arial,sans-serif;font-weight:400;font-size:84px;letter-spacing:5px;color:var(--ink);line-height:1;white-space:nowrap}

.slide{position:absolute;width:478px;height:269px;overflow:hidden;box-shadow:0 12px 24px rgba(0,0,0,.28),0 2px 6px rgba(0,0,0,.12);background:var(--white)}
.col-l{left:73px}.col-r{left:642px}
.row1{top:358px}.row2{top:700px}.row3{top:1041px}.row4{top:1382px}.row5{top:1724px}
.photo{position:absolute}
.label{position:absolute;font-family:"Montserrat",Arial,sans-serif;font-size:4.6px;letter-spacing:.6px;color:var(--muted);text-transform:uppercase}
.foot{position:absolute;bottom:17px;font-family:"Montserrat",Arial,sans-serif;font-size:4.6px;letter-spacing:.4px;color:var(--muted)}
.foot.l{left:24px}.foot.r{right:24px}
.fine{position:absolute;font-size:4.5px;line-height:1.95;text-align:justify;color:var(--white)}
.fine.dark{color:var(--muted)}
.fine.olive{color:var(--olive)}
.h-big{position:absolute;font-weight:400;font-size:25px;line-height:1.4;color:var(--heading)}
.h-big.light{color:var(--white)}

.badge{position:absolute;display:flex;align-items:center;gap:5px}
.badge .ring{border:1.5px solid var(--gold);border-radius:50%;flex:none}
.badge .bname{font-family:"Open Sans",Arial,sans-serif;font-weight:600;color:var(--gold);line-height:1.1;white-space:nowrap}
.badge.sm .ring{width:9px;height:9px;border-width:1px}
.badge.sm .bname{font-size:5px}

/* slide 1 */
.cover .photo{inset:0;background:linear-gradient(180deg,#c9c1b3 0%,#a29a8d 30%,#77716a 60%,#3b3834 100%)}
.cover .band{position:absolute;left:0;top:60px;width:419px;height:150px;background:rgba(70,68,64,.55)}
.cover .base{position:absolute;left:0;top:210px;width:478px;height:59px;background:rgba(30,29,27,.55)}
.cover .badge .ring{width:26px;height:26px}
.cover .badge .bname{font-size:9px}
.cover .title{position:absolute;left:178px;top:106px;width:230px;text-align:center;color:var(--white);font-weight:300;font-size:15.5px;line-height:1.55;letter-spacing:.3px}
.cover .title .sub{display:block;font-weight:400;font-size:13px;letter-spacing:1.2px;margin-top:5px}

/* slide 2 */
.welcome{background:var(--night)}
.welcome .photo{left:0;top:60px;width:357px;height:137px;background:linear-gradient(90deg,#9a948b 0%,#857e74 40%,#a7a093 75%,#958f84 100%)}
.welcome .hello{position:absolute;left:30px;top:122px;font-weight:600;font-size:27px;color:var(--white)}
.welcome .badge .ring{width:16px;height:16px}
.welcome .badge .bname{font-size:7px}

/* slide 3 */
.toc .photo{left:160px;top:0;width:160px;height:269px;background:linear-gradient(180deg,#efece6 0%,#d8d2c8 40%,#6d6458 75%,#3f3a33 100%)}
.toc .panel{position:absolute;left:320px;top:0;width:158px;height:269px;background:var(--panel)}
.toc ol{position:absolute;left:349px;top:78px;list-style:none;color:var(--white);font-size:7.4px;letter-spacing:.5px;line-height:19.1px}

/* slide 4 */
.services .panel{position:absolute;left:201px;top:0;width:277px;height:269px;background:var(--panel)}
.services .photo{left:162px;width:81px;height:72px}
.services .s-title{position:absolute;left:265px;font-size:9.6px;color:var(--white)}
.services .fine{left:265px;width:162px}

/* slide 5 */
.dest-a{background:var(--paper)}
.dest-a .photo{top:21px;width:93px;height:133px}
.dest-a .band{position:absolute;left:0;top:177px;width:478px;height:92px;background:var(--panel)}
.dest-a .heading{position:absolute;left:80px;top:204px;font-size:19px;color:var(--white)}

/* slide 6 */
.dest-b .panel{position:absolute;left:0;top:0;width:196px;height:269px;background:var(--panel)}
.dest-b .photo{width:94px;height:62px}

/* slide 7 */
.ceo .panel{position:absolute;left:134px;top:0;width:344px;height:269px;background:var(--panel)}
.ceo .portrait{position:absolute;left:172px;top:51px;width:98px;height:98px;border-radius:50%;background:radial-gradient(circle at 50% 45%,#e9e7e4 0%,#b9b6b1 55%,#6f6c68 100%)}

/* slide 8 */
.bullets{background:var(--panel-light)}
.bullets .photo{left:38px;top:37px;width:145px;height:193px;background:linear-gradient(180deg,#9ec3dc 0%,#7fa46f 45%,#c9bda8 70%,#5c8fa2 100%)}
.bullets .card{position:absolute;left:183px;top:37px;width:241px;height:193px;background:var(--white)}
.bullets .card h3{position:absolute;left:22px;top:27px;font-weight:700;font-size:13.5px;color:var(--olive);letter-spacing:-.1px;white-space:nowrap}
.bullets .item{position:absolute;left:22px;display:flex;gap:9px;align-items:flex-start;width:210px}
.bullets .item svg{flex:none}
.bullets .item p{font-size:4.6px;line-height:1.9;color:var(--olive)}

/* slide 9 */
.packages .photo{left:168px;top:0;width:310px;height:269px;background:linear-gradient(200deg,#dfb6a6 0%,#b8a6ad 30%,#8f8a86 55%,#3f87b7 75%,#6f4e3c 100%)}
.packages .note{position:absolute;left:168px;top:134px;width:135px;height:135px;background:var(--paper)}

/* slide 10 */
.contact .panel{position:absolute;left:0;top:0;width:238px;height:269px;background:var(--panel)}
.contact .photo{left:238px;top:0;width:240px;height:269px;background:linear-gradient(135deg,#b9c6c8 0%,#d9d6cf 40%,#9f8a78 70%,#4a4846 100%)}
.contact .c-head{position:absolute;font-family:"Montserrat",Arial,sans-serif;font-size:5.8px;letter-spacing:.8px;color:#e4e4e4}
.contact .c-body{position:absolute;font-size:4.3px;line-height:1.95;color:#eeeeee}
</style>
</head>
<body>

<header>
  <div class="brand-mark"><span class="dot"></span><span class="name">Meridian Hospitality Group</span></div>
  <h1 class="sheet-title">POWERPOINT TEMPLATE</h1>
</header>

<!-- Slide 1: cover -->
<section class="slide cover col-l row1">
  <div class="photo" role="img" aria-label="Sepia landscape above a sea of clouds"></div>
  <div class="band"></div>
  <div class="base"></div>
  <div class="badge" style="left:26px;top:118px"><span class="ring"></span><span class="bname">Velour Leisure Co.</span></div>
  <p class="title">YOUR CAN PLACE THE<br>PRESENTATION TITLE HERE<span class="sub">Your master subtitle here</span></p>
  <span class="foot l" style="color:#5b5852">www.velourleisure.com</span>
</section>

<!-- Slide 2: welcome -->
<section class="slide welcome col-r row1">
  <span class="label" style="left:24px;top:21px">Velour Leisure</span>
  <div class="photo" role="img" aria-label="Two travellers walking along a coastal cliff"></div>
  <p class="hello">Welcome to</p>
  <div class="badge" style="left:232px;top:121px"><span class="ring"></span><span class="bname">Velour Leisure Co.</span></div>
  <p class="fine" style="left:372px;top:63px;width:80px;text-align:left">Every journey we plan begins with listening. Our team shapes each stay around your pace, pairing quiet suites, private dining and curated excursions so that every guest feels expected, welcomed and entirely at ease from arrival to departure. Discreet service, handpicked destinations and thoughtful details come together in every itinerary we design for travellers who value comfort.</p>
  <span class="foot l">www.velourleisure.com</span><span class="foot r">page: 2</span>
</section>

<!-- Slide 3: table of content -->
<section class="slide toc col-l row2">
  <span class="label" style="left:24px;top:21px">Velour Leisure</span>
  <h2 class="h-big" style="left:24px;top:100px">Table of<br>content</h2>
  <div class="photo" role="img" aria-label="Moorish archway with white curtains and lounge chairs"></div>
  <div class="panel"></div>
  <div class="badge sm" style="left:432px;top:24px"><span class="ring"></span><span class="bname">Velour</span></div>
  <ol>
    <li>1. About Luxury</li><li>2. What We do</li><li>3. Our Team</li><li>4. Our Services</li><li>5. Our destinations</li><li>6. Our Packages</li><li>7. Contact</li>
  </ol>
  <span class="foot l">www.velourleisure.com</span><span class="foot r" style="color:#9a9a9a">page: 3</span>
</section>

<!-- Slide 4: what we do -->
<section class="slide services col-r row2">
  <span class="label" style="left:24px;top:26px">Velour Leisure</span>
  <h2 class="h-big" style="left:25px;top:72px;line-height:1.45">What<br>We<br>Do</h2>
  <div class="panel"></div>
  <div class="photo" style="top:20px;background:linear-gradient(160deg,#e7c58d 0%,#a8825a 50%,#3f4648 100%)" role="img" aria-label="Traveller relaxing in an airport lounge"></div>
  <div class="photo" style="top:98px;background:linear-gradient(180deg,#8fb6d6 0%,#d3cbbd 50%,#4e8fa8 100%)" role="img" aria-label="Resort villa with palm trees and pool"></div>
  <div class="photo" style="top:176px;background:linear-gradient(180deg,#9a4f54 0%,#6c8b5a 45%,#e1dbd1 100%)" role="img" aria-label="Breakfast table set beside a pool"></div>
  <div class="badge sm" style="left:432px;top:24px"><span class="ring"></span><span class="bname">Velour</span></div>
  <p class="s-title" style="top:29px">Your service number 01</p>
  <p class="fine" style="top:45px">Private transfers, tailored stays and attentive hosts who handle every detail, so your time is spent enjoying the destination rather than planning it.</p>
  <p class="s-title" style="top:107px">Your service number 02</p>
  <p class="fine" style="top:123px">Private transfers, tailored stays and attentive hosts who handle every detail, so your time is spent enjoying the destination rather than planning it.</p>
  <p class="s-title" style="top:185px">Your service number 03</p>
  <p class="fine" style="top:201px">Private transfers, tailored stays and attentive hosts who handle every detail, so your time is spent enjoying the destination rather than planning it.</p>
  <span class="foot l">www.velourleisure.com</span><span class="foot r" style="color:#9a9a9a">page: 4</span>
</section>

<!-- Slide 5: destinations (gallery) -->
<section class="slide dest-a col-l row3">
  <div class="photo" style="left:22px;background:linear-gradient(180deg,#efece6,#6d6458)" role="img" aria-label="Moorish archway with curtains"></div>
  <div class="photo" style="left:136px;background:linear-gradient(180deg,#d9b5a6,#9b9aa5 50%,#3c8bc0)" role="img" aria-label="Infinity pool at sunset"></div>
  <div class="photo" style="left:249px;background:linear-gradient(180deg,#8fb6d6,#7a9a5c 45%,#b8514f 80%,#e6e0d6)" role="img" aria-label="Breakfast by the pool under palms"></div>
  <div class="photo" style="left:363px;background:linear-gradient(180deg,#d9c7a4,#7a3a2c 55%,#4c2a22)" role="img" aria-label="Elegant restaurant dining room"></div>
  <div class="band"></div>
  <div class="badge sm" style="left:22px;top:218px"><span class="ring" style="width:14px;height:14px"></span><span class="bname">Velour</span></div>
  <p class="heading">Destinations</p>
  <p class="fine" style="left:226px;top:189px;width:229px">Every journey we plan begins with listening. Our team shapes each stay around your pace, pairing quiet suites, private dining and curated excursions so that every guest feels expected, welcomed and entirely at ease from arrival to departure.</p>
  <span class="foot l" style="color:#7f8183">www.velourleisure.com</span><span class="foot r" style="color:#8a8c8e">page: 5</span>
</section>

<!-- Slide 6: destinations (grid) -->
<section class="slide dest-b col-r row3">
  <div class="panel"></div>
  <span class="label" style="left:24px;top:21px;color:#9a9c9e">Velour Leisure</span>
  <div class="badge" style="left:62px;top:58px"><span class="ring" style="width:18px;height:18px"></span><span class="bname" style="font-size:7px">Velour</span></div>
  <h2 class="h-big light" style="left:24px;top:106px;font-size:22px">Destinations</h2>
  <p class="fine" style="left:24px;top:142px;width:160px">Every journey we plan begins with listening. Our team shapes each stay around your pace, pairing quiet suites, private dining and curated excursions so that every guest feels expected, welcomed and entirely at ease from arrival to departure. Discreet service, handpicked destinations and thoughtful details come together in every itinerary we design for travellers who value comfort.</p>
  <div class="photo" style="left:219px;top:25px;background:linear-gradient(180deg,#efece6,#6d6458)" role="img" aria-label="Moorish archway lounge"></div>
  <div class="photo" style="left:337px;top:25px;background:linear-gradient(180deg,#d9c7a4,#7a3a2c)" role="img" aria-label="Restaurant dining room"></div>
  <div class="photo" style="left:219px;top:100px;background:linear-gradient(180deg,#d9b5a6,#3c8bc0)" role="img" aria-label="Infinity pool at sunset"></div>
  <div class="photo" style="left:337px;top:100px;background:linear-gradient(180deg,#8fb6d6,#d3cbbd 55%,#4e8fa8)" role="img" aria-label="Resort villa with pool"></div>
  <div class="photo" style="left:219px;top:176px;background:linear-gradient(180deg,#9a4f54,#6c8b5a 45%,#e1dbd1)" role="img" aria-label="Poolside breakfast table"></div>
  <div class="photo" style="left:337px;top:176px;background:linear-gradient(180deg,#86aed4,#9fc2de 55%,#6e8e4c)" role="img" aria-label="Couple walking on a green meadow"></div>
  <span class="foot l" style="color:#9a9c9e">www.velourleisure.com</span><span class="foot r">page: 6</span>
</section>

<!-- Slide 7: about our CEO -->
<section class="slide ceo col-l row4">
  <span class="label" style="left:24px;top:21px">Velour Leisure</span>
  <p class="fine dark" style="left:25px;top:52px;width:95px">Every journey we plan begins with listening. Our team shapes each stay around your pace, pairing quiet suites, private dining and curated excursions so that every guest feels expected, welcomed and entirely at ease from arrival to departure.</p>
  <div class="panel"></div>
  <div class="portrait" role="img" aria-label="Portrait of the chief executive in a bow tie"></div>
  <div class="badge sm" style="left:432px;top:24px"><span class="ring"></span><span class="bname">Velour</span></div>
  <h2 class="h-big light" style="left:283px;top:66px;font-size:25px;line-height:1.4">About<br>our CEO</h2>
  <p class="fine" style="left:177px;top:170px;width:275px">Every journey we plan begins with listening. Our team shapes each stay around your pace, pairing quiet suites, private dining and curated excursions so that every guest feels expected, welcomed and entirely at ease from arrival to departure. Discreet service, handpicked destinations and thoughtful details come together in every itinerary we design for travellers who value comfort.</p>
  <span class="foot l">www.velourleisure.com</span><span class="foot r" style="color:#9a9a9a">page: 7</span>
</section>

<!-- Slide 8: bullets -->
<section class="slide bullets col-r row4">
  <span class="label" style="left:24px;top:21px;color:#9a9c9e">Velour Leisure</span>
  <div class="badge sm" style="left:432px;top:24px"><span class="ring"></span><span class="bname">Velour</span></div>
  <div class="photo" role="img" aria-label="Thatched beach villa with pool and palm trees"></div>
  <div class="card">
    <h3>Bullets options slide&nbsp; design</h3>
    <div class="item" style="top:62px"><svg width="11" height="11" viewBox="0 0 11 11"><circle cx="5.5" cy="5.5" r="4.8" fill="none" stroke="#5a5636" stroke-width=".8"/><path d="M3.2 5.6l1.6 1.6 3-3.3" fill="none" stroke="#5a5636" stroke-width=".9"/></svg><p>A presentation template created with attentive detail to provide a new experience for users. Hopefully this presentation can help you and bring.</p></div>
    <div class="item" style="top:94px"><svg width="11" height="11" viewBox="0 0 11 11"><circle cx="5.5" cy="5.5" r="4.8" fill="none" stroke="#5a5636" stroke-width=".8"/><path d="M3.2 5.6l1.6 1.6 3-3.3" fill="none" stroke="#5a5636" stroke-width=".9"/></svg><p>A presentation template created with attentive detail to provide a new experience for users. Hopefully this presentation can help you and bring.</p></div>
    <div class="item" style="top:126px"><svg width="11" height="11" viewBox="0 0 11 11"><circle cx="5.5" cy="5.5" r="4.8" fill="none" stroke="#5a5636" stroke-width=".8"/><path d="M3.2 5.6l1.6 1.6 3-3.3" fill="none" stroke="#5a5636" stroke-width=".9"/></svg><p>A presentation template created with attentive detail to provide a new experience for users. Hopefully this presentation can help you and bring.</p></div>
    <div class="item" style="top:158px"><svg width="11" height="11" viewBox="0 0 11 11"><circle cx="5.5" cy="5.5" r="4.8" fill="none" stroke="#5a5636" stroke-width=".8"/><path d="M3.2 5.6l1.6 1.6 3-3.3" fill="none" stroke="#5a5636" stroke-width=".9"/></svg><p>A presentation template created with attentive detail to provide a new experience for users. Hopefully this presentation can help you and bring.</p></div>
  </div>
  <span class="foot l" style="color:#a3a4a5">www.velourleisure.com</span><span class="foot r" style="color:#dcdcdc">page: 8</span>
</section>

<!-- Slide 9: our packages -->
<section class="slide packages col-l row5">
  <span class="label" style="left:24px;top:21px">Velour Leisure</span>
  <h2 class="h-big" style="left:25px;top:76px">Our<br>Packages</h2>
  <p class="fine olive" style="left:24px;top:154px;width:130px">Every journey we plan begins with listening. Our team shapes each stay around your pace, pairing quiet suites, private dining and curated excursions so that every guest feels expected, welcomed and entirely at ease from arrival to departure.</p>
  <div class="photo" role="img" aria-label="Infinity pool overlooking the sea at dusk"></div>
  <div class="badge sm" style="left:432px;top:24px"><span class="ring"></span><span class="bname">Velour</span></div>
  <div class="note"></div>
  <p class="fine olive" style="left:199px;top:154px;width:75px">Discreet service, handpicked destinations and thoughtful details come together in every itinerary we design for travellers who value comfort.</p>
  <span class="foot l">www.velourleisure.com</span>
</section>

<!-- Slide 10: contact (TeskaPoint) -->
<section class="slide contact col-r row5">
  <div class="panel"></div>
  <div class="badge" style="left:28px;top:42px"><span class="ring" style="width:20px;height:20px"></span><span class="bname" style="font-size:7px">TeskaPoint</span></div>
  <h2 class="h-big light" style="left:29px;top:92px;font-size:25px">Contact</h2>
  <p class="c-head" style="left:29px;top:132px">OFFICE HOURS</p>
  <p class="c-body" style="left:29px;top:141px">Monday – Thursday<br>08:00 – 17:00</p>
  <p class="c-head" style="left:123px;top:132px">OUR ADDRESS</p>
  <p class="c-body" style="left:123px;top:141px">48 Harbour Crest Way<br>Brookfield, CA 90210<br>United States</p>
  <p class="c-head" style="left:29px;top:187px">GET IN TOUCH</p>
  <p class="c-body" style="left:29px;top:196px">(+1) 555-010 240 100<br>(+1) 555-010 240 189<br>(+1) 555-010 240 180</p>
  <p class="c-head" style="left:123px;top:187px">FOLLOW US</p>
  <p class="c-body" style="left:123px;top:196px">@teskapoint<br>www.teskapoint.com<br>office@teskapoint.com</p>
  <div class="photo" role="img" aria-label="Hands typing on a laptop keyboard in a bright office"></div>
  <span class="foot l" style="color:#7f8183">www.teskapoint.com</span>
</section>

</body>
</html>
```